Website Makeover for Local small business Law Enforcement Vendor

We are a very small business (2-3 employees) that provides training and study products to police officers study for promotion exams, as well as other law enforcement training. We currently use NestHarbor as our hosting company and we use one of there template makers for our web design. So your design will have to be compatible and easy for a novice to upload in place of the current NestHarbor template. This is vital. You will need to provide detailed instructions on how to convert your design to our existing website.

The website has an accompanying web store were customers can buy products, ultimately we'd like a full integration between the main website and the on-line store. However, we can't afford to have our site or store down for any period of time.

Our web address is www.trelvanrankprep.us It is simple and unprofessional. We'd like it to be modern and inviting.

We have four main categories of services/products:

1. Police Promotion Exam Preparation
2. Police Training
3. Police Entrance Exam Services
4. Police Department Services

We are open to your expertise and suggestions. We don't have many photos/graphics to offer you.
Updates

Target Market(s)

Police officers and Police Departments

Industry/Entity Type

Small Business

Requirements
Must have
• Easy conversion to existing NestHarbor hosting - with detailed instructions.

Link to our webstore - unless you can better integrate to existing site.

The ability for a novice to modify content and load updates with ease.
Nice to have
• The ability to post PDF's and/or Word documents for download by others (registration forms etc.)

```html
<!DOCTYPE html>
<html lang="en">
<head>
<meta charset="utf-8">
<title>Carrowell Consulting, LLC</title>
<link href="https://fonts.googleapis.com/css2?family=Open+Sans:wght@400;600;700&family=Oswald:wght@600&family=Lora:ital@1&display=swap" rel="stylesheet">
<style>
:root{
  --page:#ededed;
  --header-dark:#0d2f6e;
  --header-mid:#1d5aa6;
  --header-light:#3b84c8;
  --nav-top:#4a4a4a;
  --nav-bottom:#242424;
  --ink:#333333;
  --ink-soft:#555555;
  --white:#ffffff;
  --line:#d8d8d8;
  --panel:#f2f2f2;
  --badge-gold:#f2c417;
  --badge-blue:#1d3f8a;
}
*{margin:0;padding:0;box-sizing:border-box}
html,body{width:1169px;height:1200px;overflow:hidden}
body{background:var(--page);font-family:"Open Sans",Arial,sans-serif;color:var(--ink);position:relative}
.abs{position:absolute}

/* header */
.site-header{left:0;top:0;width:1169px;height:122px;
  background:radial-gradient(ellipse 420px 140px at 640px 50px,var(--header-light),transparent 75%),
  linear-gradient(180deg,var(--header-mid),var(--header-dark));border-bottom:3px solid #9cb6d6}
.brand-badge{left:210px;top:12px;width:86px;height:96px;border-radius:10px;background:var(--badge-blue);
  border:4px solid var(--badge-gold);display:flex;align-items:center;justify-content:center;text-align:center}
.brand-badge span{color:var(--white);font-weight:700;font-size:11px;line-height:1.3}
.tagline{left:326px;top:54px;font-family:"Lora",Georgia,serif;font-style:italic;color:#dfe9f5;font-size:18px}
.social-top{left:864px;top:10px;display:flex;gap:4px}
.social-top i{display:block;width:22px;height:22px;border-radius:50%;background:#123a74;border:1px solid #0a2752}

/* nav */
.main-nav{left:192px;top:120px;width:786px;height:40px;background:linear-gradient(var(--nav-top),var(--nav-bottom));
  border-radius:0 0 4px 4px;box-shadow:0 3px 5px rgba(0,0,0,.35);display:flex;align-items:center;
  justify-content:space-between;padding:0 34px 0 19px}
.main-nav a{color:var(--white);text-decoration:none;font-size:9.5px;font-weight:600;letter-spacing:.2px;white-space:nowrap}

/* slider */
.slider{left:202px;top:176px;width:765px;height:274px;background:var(--white);border-radius:6px;box-shadow:0 0 3px rgba(0,0,0,.15)}
.slide-image{left:7px;top:8px;width:752px;height:234px;background:linear-gradient(180deg,#cfd3d6 0%,#b7a08e 35%,#4a4c52 60%,#1f2024 80%,#9c9c9c 100%)}
.slider-arrows{left:8px;top:250px;display:flex;gap:4px}
.slider-arrows span{width:18px;height:18px;border-radius:50%;background:#e4e4e4;border:1px solid #cfcfcf;display:flex;align-items:center;justify-content:center}
.slider-dots{right:18px;top:255px;display:flex;gap:1px}
.slider-dots i{width:10px;height:10px;border-radius:50%;border:1px solid #ccc;background:#f4f4f4}
.slider-dots i.on{background:#cfcfcf}

/* intro */
.intro-title{left:0;width:1169px;top:460px;text-align:center;font-size:20px;color:#3a3a3a;letter-spacing:.3px}
.intro-sub{left:0;width:1169px;top:489px;text-align:center;font-size:10px;color:#333}
.intro-rule{left:235px;top:516px;width:700px;height:2px;background:linear-gradient(90deg,transparent,var(--line),transparent)}

/* service cards */
.card-title{font-size:13px;font-weight:700;color:#333;white-space:nowrap}
.card-image{display:block}
.card-text{font-size:9.5px;line-height:18px;color:var(--ink-soft)}

/* store */
.store-title{left:749px;top:764px;font-family:"Oswald",Impact,sans-serif;font-weight:600;font-size:20px;color:#222;letter-spacing:-.2px}
.store-image{left:742px;top:793px;width:212px;height:130px;background:linear-gradient(135deg,#e6e6e6,#c9c9c9 45%,#e9c6d4 70%,#bfe5f2)}
.store-button{left:790px;top:828px;width:132px;height:46px;background:rgba(90,90,90,.85);color:var(--white);
  font-family:"Oswald",Impact,sans-serif;font-weight:600;font-size:14px;display:flex;align-items:center;justify-content:center}

/* footer */
.site-footer{left:185px;top:943px;width:799px;height:215px;background:var(--panel);border:1px solid #e2e2e2}
.foot-head{font-size:11px;font-weight:700;color:#222;letter-spacing:.5px}
.foot-text{font-size:9px;line-height:17px;color:#444;letter-spacing:.2px}
.contact-list{left:817px;top:1015px;list-style:none}
.contact-list li{display:flex;align-items:center;gap:10px;height:17.5px;font-size:10px;color:#444;letter-spacing:.4px}
.contact-list svg{width:13px;height:13px}
.social-row{display:flex;gap:2px}
.social-row i{width:11px;height:11px;display:block;background:#4a7dc0}
.social-row i:first-child{background:#e88a25}
.legal{top:1168px;font-size:9px;color:#555;letter-spacing:.3px}
.legal-links{right:216px;top:1168px;font-size:9px;color:#555;word-spacing:2px}
</style>
</head>
<body>

<header class="site-header abs">
  <div class="brand-badge abs"><span>CARROWELL<br>CONSULTING</span></div>
  <div class="tagline abs">Excel with exellence</div>
  <div class="social-top abs"><i></i><i></i><i></i><i></i></div>
</header>

<nav class="main-nav abs">
  <a>HOME</a><a>ABOUT US</a><a>FREE RESOURCES</a><a>POLICE PROMOTIONS</a><a>POLICE EMPLOYMENT</a><a>DEPARTMENT SERVICES</a><a>UPCOMING COURSES</a><a>CONTACT US</a>
</nav>

<section class="slider abs">
  <div class="slide-image abs" role="img" aria-label="Two police patrol vehicles with lights on parked in front of a brick building"></div>
  <div class="slider-arrows abs">
    <span><svg width="8" height="8" viewBox="0 0 8 8"><path d="M5 1 2 4l3 3" fill="none" stroke="#555" stroke-width="1.4"/></svg></span>
    <span><svg width="8" height="8" viewBox="0 0 8 8"><path d="M3 1l3 3-3 3" fill="none" stroke="#555" stroke-width="1.4"/></svg></span>
  </div>
  <div class="slider-dots abs"><i></i><i></i><i class="on"></i><i></i></div>
</section>

<h1 class="intro-title abs" style="font-weight:400">CARROWELL CONSULTING, LLC</h1>
<p class="intro-sub abs">POLICE PROMOTIONS, TRAINING, SELECTION &amp; more</p>
<div class="intro-rule abs"></div>

<article class="service abs" style="left:209px;top:568px;width:230px">
  <h2 class="card-title">POLICE PROMOTIONAL PREPARATION</h2>
  <div class="card-image" style="margin-top:9px;width:228px;height:81px;background:linear-gradient(180deg,#8fa872,#d5d8d6 55%,#6b6d70)" role="img" aria-label="Police patrol car with light bar on a road"></div>
  <p class="card-text" style="margin-top:18px">We have quickly become the leader in Police Promotional Preparation in Massachusetts.</p>
</article>

<article class="service abs" style="left:485px;top:568px;width:225px">
  <h2 class="card-title">POLICE EMPLOYMENT PREPARATION</h2>
  <div class="card-image" style="margin-top:9px;width:220px;height:81px;background:linear-gradient(90deg,#d9dadb,#8b8d90 50%,#c8c4bf)" role="img" aria-label="Officer using an in-car computer in a patrol vehicle"></div>
  <p class="card-text" style="margin-top:15px;padding-left:3px">Exam preparation, interviewing &amp; assessment centers, career path and job search</p>
</article>

<article class="service abs" style="left:747px;top:568px;width:222px">
  <h2 class="card-title">POLICE TRAINING &amp; EDUCATION</h2>
  <div class="card-image" style="margin-top:9px;width:205px;height:81px;background:linear-gradient(160deg,#6f9ad0,#8c8f93 50%,#d9773a)" role="img" aria-label="Motorcycle officer riding past a traffic barrel"></div>
  <p class="card-text" style="margin-top:15px">Advanced &amp; Specialized legal training for State, Municipal and Campus Police. We can custom tailor training to the needs or your agency.</p>
</article>

<article class="service abs" style="left:209px;top:748px;width:230px">
  <h2 class="card-title">LAW ENFORCEMENT AGENCY SERVICES</h2>
  <div class="card-image" style="margin-top:9px;width:235px;height:82px;background:linear-gradient(90deg,#b9bcbf,#2c2d31 45%,#8a6d4c 60%,#a6a9ad)" role="img" aria-label="K-9 officer with police dog beside parked cars"></div>
  <p class="card-text" style="margin-top:18px">Training, Entrance and Promotional Exam creation and administration, Assessment Centers and selection assistance.</p>
</article>

<article class="service abs" style="left:485px;top:748px;width:225px">
  <h2 class="card-title">UPCOMING COURSE SCHEDULE</h2>
  <div class="card-image" style="margin-top:9px;width:218px;height:82px;background:linear-gradient(180deg,#c89a55,#f0e2c4 50%,#a7773f)" role="img" aria-label="Open book with fanned pages in front of stacked books"></div>
  <p class="card-text" style="margin-top:20px;padding-left:3px">Lorem ipsum dolor sit amet, consectetur elit. Nullam ac vehicula turpis.</p>
</article>

<div class="store-title abs">VISIT OUR ON-LINE STORE</div>
<div class="store-image abs" role="img" aria-label="Online shopper with laptop and shopping bags"></div>
<div class="store-button abs">Visit store &gt;</div>

<footer class="site-footer abs">
  <div class="abs" style="left:36px;top:38px">
    <h3 class="foot-head">Location</h3>
    <p class="foot-text" style="margin-top:22px">Carrowell Consulting, LLC<br>P.O. Box 517<br>Brookfield, MA 01506</p>
  </div>
  <div class="abs" style="left:236px;top:38px;width:180px">
    <h3 class="foot-head">FREE</h3>
    <p class="foot-text" style="margin-top:22px">FOR FREE Philadelphia Exam Practice Questions - Send an email to questions@trelvanrankprep.us and type in PHILLY.</p>
  </div>
  <div class="abs" style="left:433px;top:38px;width:170px">
    <h3 class="foot-head" style="line-height:14px">VIEW SOME OF OUR MANY SUCCESS STORIES</h3>
    <div style="margin:12px 0 0 32px;width:88px;height:88px;background:radial-gradient(circle,#3b6fe0 30%,#8fb3f2 55%,transparent 70%)" role="img" aria-label="Blue police emergency light"></div>
  </div>
  <div class="abs" style="left:631px;top:38px">
    <h3 class="foot-head" style="font-weight:600;letter-spacing:1px">Get in Touch</h3>
  </div>
</footer>

<ul class="contact-list abs">
  <li><svg viewBox="0 0 13 13"><path d="M1 4c0-2 2-3 5.5-3S12 2 12 4l-3 .5-.5-1.5h-4L4 4.5zM3 6h7l1.5 5h-10z" fill="#444"/></svg>1-800-555-5555</li>
  <li><svg viewBox="0 0 13 13"><rect x="1" y="3" width="11" height="8" fill="#444"/><path d="M1 3l5.5 4.5L12 3" fill="none" stroke="#f2f2f2"/></svg>you@yoursite.com</li>
  <li><svg viewBox="0 0 13 13"><path d="M2 11l1-3 6-6 2 2-6 6z" fill="#444"/></svg>Contact Form</li>
  <li><svg viewBox="0 0 13 13"><circle cx="6.5" cy="6.5" r="5" fill="#444"/></svg>YourSkypeUserID</li>
  <li><svg viewBox="0 0 13 13"><rect x="1" y="4" width="6" height="4" rx="2" fill="none" stroke="#444" stroke-width="1.5"/><rect x="6" y="5" width="6" height="4" rx="2" fill="none" stroke="#444" stroke-width="1.5"/></svg>
    <span class="social-row"><i></i><i></i><i></i><i></i><i></i><i></i></span></li>
</ul>

<p class="legal abs" style="left:210px">(C) 2012 All rights reserved.</p>
<p class="legal-links abs">Terms of Service &nbsp;|&nbsp; Privacy Policy &nbsp;|&nbsp; Contact Us</p>

</body>
</html>
```